Brambury Logistics

Create a modern, simple, Elegant business card design for my business.

Services: Tamo Trucks, Transport, Contract Logistics,

Industry/Entity Type

Business

Contact Information for Business Card

Include all details same as old card plus new website address: www.bramburylogistics.com.au

Requirements
Must have
• Similar colors to Logo.

```html
<!DOCTYPE html>
<html lang="en">
<head>
<meta charset="utf-8">
<title>Brambury Logistics — Business Card</title>
<link href="https://fonts.googleapis.com/css2?family=Arimo:wght@400;700&display=swap" rel="stylesheet">
<style>
  :root {
    --backdrop: #e9eaec;
    --card: #ffffff;
    --brand-blue: #1f8fd0;
    --brand-grey: #a6a7a9;
    --ink: #111111;
    --shadow: rgba(0, 0, 0, 0.18);
  }
  * { box-sizing: border-box; margin: 0; padding: 0; }
  html, body {
    width: 1200px;
    height: 1200px;
    overflow: hidden;
    background: var(--backdrop);
    font-family: "Arimo", Arial, sans-serif;
  }
  .sheet {
    width: 1200px;
    height: 1200px;
    display: flex;
    flex-direction: column;
    align-items: center;
    justify-content: center;
    gap: 64px;
  }
  .card {
    position: relative;
    width: 900px;
    height: 514px;
    background: var(--card);
    box-shadow: 0 6px 22px var(--shadow);
    overflow: hidden;
  }
  .card-bands {
    position: absolute;
    inset: 0;
    width: 100%;
    height: 100%;
  }
  .band-grey { fill: var(--brand-grey); }
  .band-blue { fill: var(--brand-blue); }

  .wordmark {
    position: absolute;
    font-weight: 700;
    color: var(--brand-grey);
    letter-spacing: 0.5px;
    white-space: nowrap;
  }
  .card-front .wordmark {
    left: 150px;
    top: 210px;
    font-size: 58px;
  }
  .card-back .wordmark {
    left: 60px;
    top: 150px;
    font-size: 30px;
  }

  .services {
    position: absolute;
    right: 60px;
    top: 128px;
    text-align: right;
    color: var(--ink);
    font-size: 24px;
    line-height: 1.25;
  }
  .services-title {
    color: var(--brand-blue);
    font-weight: 700;
    font-size: 26px;
  }

  .contact {
    position: absolute;
    right: 60px;
    top: 284px;
    color: var(--ink);
    font-size: 22px;
    line-height: 30px;
    list-style: none;
  }
  .contact-item {
    display: flex;
    justify-content: flex-end;
    align-items: center;
    gap: 8px;
    white-space: nowrap;
  }
  .contact-icon {
    width: 20px;
    height: 20px;
    flex: none;
  }
</style>
</head>
<body>
<main class="sheet">

  <section class="card card-front" aria-label="Business card front">
    <svg class="card-bands" viewBox="0 0 900 514" preserveAspectRatio="none" aria-hidden="true">
      <polygon class="band-grey" points="0,0 640,0 0,190"/>
      <polygon class="band-blue" points="0,190 640,0 700,0 0,212"/>
      <polygon class="band-grey" points="900,330 900,514 150,514"/>
      <polygon class="band-blue" points="900,300 900,330 150,514 90,514"/>
    </svg>
    <div class="wordmark">Brambury Logistics</div>
  </section>

  <section class="card card-back" aria-label="Business card back">
    <svg class="card-bands" viewBox="0 0 900 514" preserveAspectRatio="none" aria-hidden="true">
      <polygon class="band-grey" points="380,0 900,0 900,90"/>
      <polygon class="band-blue" points="320,0 380,0 900,90 900,115"/>
      <polygon class="band-grey" points="0,300 700,514 0,514"/>
      <polygon class="band-blue" points="0,275 760,514 700,514 0,300"/>
    </svg>

    <div class="wordmark">Brambury Logistics</div>

    <div class="services">
      <p class="services-title">Services:</p>
      <p>Tamo Trucks</p>
      <p>Transport</p>
      <p>Contract Logistics</p>
    </div>

    <ul class="contact">
      <li class="contact-item">
        <svg class="contact-icon" viewBox="0 0 22 22" aria-hidden="true">
          <circle cx="11" cy="11" r="11" fill="var(--brand-blue)"/>
          <path d="M7.5 5.5l2 .2.8 2.6-1.3 1a7 7 0 0 0 3.7 3.7l1-1.3 2.6.8.2 2c-.3.8-1.2 1.3-2 1.2A10 10 0 0 1 6.3 7.5c-.1-.8.4-1.7 1.2-2z" fill="#fff"/>
        </svg>
        <span>0491570263</span>
      </li>
      <li class="contact-item">
        <svg class="contact-icon" viewBox="0 0 22 22" aria-hidden="true">
          <circle cx="11" cy="11" r="11" fill="var(--brand-blue)"/>
          <rect x="5.5" y="7" width="11" height="8" rx="1" fill="#fff"/>
          <path d="M5.8 7.5l5.2 4 5.2-4" fill="none" stroke="var(--brand-blue)" stroke-width="1.2"/>
        </svg>
        <span>tess@bramburylogistics.com.au</span>
      </li>
      <li class="contact-item">
        <svg class="contact-icon" viewBox="0 0 22 22" aria-hidden="true">
          <circle cx="11" cy="11" r="11" fill="var(--brand-blue)"/>
          <circle cx="11" cy="11" r="5.5" fill="none" stroke="#fff" stroke-width="1.3"/>
          <path d="M5.5 11h11M11 5.5c-2.4 3-2.4 8 0 11M11 5.5c2.4 3 2.4 8 0 11" fill="none" stroke="#fff" stroke-width="1.1"/>
        </svg>
        <span>www.bramburylogistics.com.au</span>
      </li>
      <li class="contact-item"><span>Western Australia</span></li>
    </ul>
  </section>

</main>
</body>
</html>
```